Business Card Design Project

parking lot sealing and striping company

Industry/Entity Type

Business

Contact Information for Business Card

See pics below, blue and gray colors

```html
<!DOCTYPE html>
<html lang="en">
<head>
<meta charset="utf-8">
<title>Summit Line Paving – Business Card</title>
<link href="https://fonts.googleapis.com/css2?family=Oswald:wght@700&family=Roboto:wght@400;500&family=Roboto+Condensed:wght@400&display=swap" rel="stylesheet">
<style>
  :root {
    --stage: #1a1a1a;
    --asphalt-dark: #1f1f1f;
    --asphalt-mid: #3a3a3a;
    --paper: #f7f8f9;
    --brand-blue: #0a8fdc;
    --navy: #0f2a40;
    --white: #ffffff;
  }
  * { margin: 0; padding: 0; box-sizing: border-box; }
  html, body { width: 1200px; height: 767px; overflow: hidden; background: var(--stage); }
  .card {
    position: absolute; left: 377px; top: 248px; width: 445px; height: 270px; overflow: hidden;
  }
  .asphalt-texture {
    position: absolute; inset: 0;
    background: radial-gradient(ellipse at 40% 45%, var(--asphalt-mid) 0%, var(--asphalt-dark) 85%);
  }
  .card-shapes { position: absolute; inset: 0; }
  .brand {
    position: absolute; left: 28px; top: 33px; display: flex; align-items: center; gap: 8px;
    font-family: "Roboto", sans-serif; font-weight: 400; font-size: 19px; color: var(--brand-blue);
  }
  .brand-dot { width: 30px; height: 30px; border-radius: 50%; background: var(--white); }
  .person-name {
    position: absolute; left: 28px; top: 117px;
    font-family: "Oswald", sans-serif; font-weight: 700; font-size: 18px; color: var(--white); letter-spacing: 0.2px;
  }
  .person-title, .address, .contact-list {
    font-family: "Roboto Condensed", sans-serif; color: var(--white);
  }
  .person-title { position: absolute; left: 28px; top: 141px; font-size: 10px; }
  .address { position: absolute; left: 28px; top: 172px; font-size: 11.5px; }
  .contact-list { position: absolute; left: 28px; top: 195px; list-style: none; font-size: 11.5px; }
  .contact-list li { display: flex; align-items: center; height: 16px; }
  .contact-list svg { width: 12px; height: 10px; margin-right: 8px; fill: var(--white); }
  .services {
    position: absolute; right: 41px; top: 41px; list-style: none; text-align: right;
    font-family: "Roboto", sans-serif; font-weight: 500; font-size: 13px; color: var(--navy);
  }
  .services li { height: 19px; line-height: 19px; }
  .services li::before { content: "»"; margin-right: 8px; }
</style>
</head>
<body>
  <div class="card">
    <div class="asphalt-texture" role="img" aria-label="Dark grey asphalt surface texture"></div>
    <svg class="card-shapes" viewBox="0 0 445 270" width="445" height="270" aria-hidden="true">
      <path d="M272,44 C232,120 238,212 290,270 H314 C258,210 238,122 272,44 Z" fill="var(--brand-blue)"/>
      <path d="M288,0 H445 V270 H310 C252,205 232,95 288,0 Z" fill="var(--paper)"/>
    </svg>

    <div class="brand"><span class="brand-dot"></span>Summit Line Paving</div>

    <div class="person-name">DANA MILLER</div>
    <div class="person-title">Managing Director</div>
    <div class="address">14/3 Harbour Lane, VIC 3050</div>
    <ul class="contact-list">
      <li><svg viewBox="0 0 12 10"><path d="M1,3 C3,0 9,0 11,3 L9,4 L8,2.5 H4 L3,4 Z M3,5 H9 L10,9 H2 Z"/></svg>Free Call: 1800 SUMMIT</li>
      <li><svg viewBox="0 0 12 10"><path d="M0,1 H12 V9 H0 Z M1,2 L6,6 L11,2 Z" fill-rule="evenodd"/></svg>dana@summitlinepaving.com</li>
      <li><svg viewBox="0 0 12 12"><circle cx="6" cy="6" r="5" fill="none" stroke="#fff" stroke-width="1.2"/><path d="M1,6 H11 M6,1 V11" stroke="#fff" stroke-width="1"/></svg>www.summitlinepaving.com</li>
    </ul>

    <ul class="services">
      <li>Asphal Bealing</li>
      <li>Crack Repair</li>
      <li>Ramp Building</li>
      <li>Line Paiing</li>
      <li>Walevwe</li>
      <li>Asphal Bealing</li>
      <li>Crack Repair</li>
      <li>Ramp Building</li>
      <li>Line Paiing</li>
      <li>Walevwe</li>
    </ul>
  </div>
</body>
</html>
```